Powerpoint Re-design

I have 2 existing powerpoint slideshows.

I need the content and branding kept however the images and design, within the content, I would like updated.

This is for a wealth creation company called Summit Harvest. The maroon colour, logo and pig must be retained.

I would like the content on each of the slides kept however the graphics and images need to be updated. Many of the images are outdated and inconsistent throughout the powerpoint.

This is a financial education based presentation delivered to everyday Australians (25 -60yo) this needs to be sharp and credible while simple and current.

View one of the slideshows at:

https://files.examplehost.net/u/58204916/1075_SH_Evening%20Workshop%20v3.pptx

and

https://files.examplehost.net/u/58204916/1075_SH_One%20Day%20Intensive%20v2.pptx
Updates

You can view slideshow at the following links

To make it more clear what I am after. The content I would like to keep the same.

The colours and logos I would like to keep the same.

The font can be changed to appear cleaner, sharper and more professional.

The images and graphics are mainly what I would like to update. Some pics are ok but others look old & too basic and this is primarily what I want updated.

These when updated must still match the content or be something similar to what is already there however a newer, sharper more professional image/graphic.

Target Market(s)

25 - 55yo, singles and couples, $30kpa - $300kpa incomes, not financially savy!

Industry/Entity Type

Financial

Requirements
Must have
• Must have existing maroon, logo and pig.
Should not have
• Not be too "busy!"

Please keep it clean and simple.

```html
<!DOCTYPE html>
<html lang="en">
<head>
<meta charset="utf-8">
<title>The win-win-win partnership — Summit Harvest</title>
<link rel="stylesheet" href="https://fonts.googleapis.com/css2?family=PT+Sans+Narrow:wght@400;700&display=swap">
<style>
  :root {
    --maroon: #6e2544;
    --maroon-dark: #4a1029;
    --maroon-light: #8a3a5c;
    --title: #5a1a36;
    --ink: #333333;
    --rule: #cfcfcf;
    --page-bg: #f4f4f4;
    --blue-top: #2f9bea;
    --blue-bottom: #0a5aa8;
    --red-top: #ff5a2a;
    --red-bottom: #cc2a00;
    --green-top: #8fd01e;
    --green-bottom: #4e9a06;
    --connector: #6e2544;
    --white: #ffffff;
  }
  * { box-sizing: border-box; margin: 0; padding: 0; }
  html, body { width: 1200px; height: 900px; overflow: hidden; }
  body {
    font-family: "PT Sans Narrow", "Arial Narrow", sans-serif;
    background: var(--page-bg);
  }
  .slide {
    position: relative;
    width: 1200px;
    height: 900px;
    overflow: hidden;
    background:
      radial-gradient(ellipse 900px 420px at 680px 260px, rgba(255,255,255,0.95), rgba(255,255,255,0) 70%),
      radial-gradient(ellipse 700px 300px at 300px 700px, rgba(225,225,225,0.7), rgba(255,255,255,0) 70%),
      linear-gradient(180deg, #f7f7f7 0%, #ececec 100%);
  }
  .top-band {
    position: absolute; left: 0; top: 0; width: 1200px; height: 100px;
    background: linear-gradient(180deg, var(--maroon-light) 0%, var(--maroon) 45%, var(--maroon-dark) 100%);
  }
  .brand {
    position: absolute; right: 48px; top: 22px;
    color: var(--white);
    font-size: 46px; font-weight: 400; letter-spacing: 0.5px;
  }
  .slide-title {
    position: absolute; left: 57px; top: 132px;
    color: var(--title);
    font-size: 52px; font-weight: 700;
  }
  .title-rule {
    position: absolute; left: 57px; top: 202px; width: 1060px; height: 2px;
    background: linear-gradient(90deg, var(--rule), rgba(207,207,207,0.2));
  }
  .subtitle {
    position: absolute; left: 636px; top: 238px;
    color: var(--ink);
    font-size: 44px; font-weight: 400;
  }
  .hero-image {
    position: absolute; left: 60px; top: 370px; width: 410px; height: 380px;
    border-radius: 45% 45% 30% 30%;
    background: radial-gradient(ellipse at 45% 40%, #ffffff 0%, #e6e6e6 55%, #bcbcbc 100%);
  }
  .diagram-lines { position: absolute; left: 0; top: 0; }
  .team-box {
    position: absolute;
    display: flex; align-items: center; justify-content: center;
    text-align: center;
    color: var(--white);
    font-size: 27px; line-height: 1.1; font-weight: 400;
    border: 1px solid rgba(255,255,255,0.7);
    border-radius: 3px;
    box-shadow: 0 2px 4px rgba(0,0,0,0.25);
    background: linear-gradient(180deg, var(--blue-top), var(--blue-bottom));
  }
  .team-box--you {
    background: linear-gradient(180deg, var(--green-top), var(--green-bottom));
    font-size: 34px;
  }
  .team-box--lead { background: linear-gradient(180deg, var(--red-top), var(--red-bottom)); }
  .bottom-band {
    position: absolute; left: 0; top: 845px; width: 1200px; height: 55px;
    background: linear-gradient(180deg, var(--maroon-light) 0%, var(--maroon) 50%, var(--maroon-dark) 100%);
  }
  .page-number {
    position: absolute; right: 30px; top: 852px;
    color: var(--white);
    font-size: 28px; font-weight: 700;
  }
</style>
</head>
<body>
  <main class="slide">
    <header class="top-band">
      <div class="brand">Summit Harvest</div>
    </header>

    <h1 class="slide-title">The win-win-win partnership</h1>
    <div class="title-rule"></div>

    <h2 class="subtitle">5 Teams Working for You</h2>

    <div class="hero-image" role="img" aria-label="Two glossy white piggy banks side by side"></div>

    <svg class="diagram-lines" width="1200" height="900" viewBox="0 0 1200 900" aria-hidden="true">
      <g stroke="var(--connector)" stroke-width="3" fill="none">
        <line x1="855" y1="412" x2="855" y2="545"/>
        <line x1="697" y1="545" x2="855" y2="545"/>
        <line x1="855" y1="545" x2="997" y2="545"/>
        <line x1="855" y1="545" x2="855" y2="723"/>
        <line x1="855" y1="545" x2="690" y2="645"/>
        <line x1="855" y1="545" x2="960" y2="618"/>
      </g>
    </svg>

    <div class="team-box team-box--you" style="left:755px; top:342px; width:197px; height:70px;">You</div>
    <div class="team-box team-box--lead" style="left:757px; top:502px; width:197px; height:86px;">Client<br>Manager</div>
    <div class="team-box" style="left:502px; top:502px; width:195px; height:86px;">Client<br>Manager</div>
    <div class="team-box" style="left:997px; top:502px; width:195px; height:86px;">Client<br>Manager</div>
    <div class="team-box" style="left:562px; top:613px; width:135px; height:86px;">Finance</div>
    <div class="team-box" style="left:951px; top:613px; width:165px; height:86px;">Property<br>Management</div>
    <div class="team-box" style="left:757px; top:723px; width:197px; height:84px;">Financial<br>Planning</div>

    <footer class="bottom-band"></footer>
    <div class="page-number">Page&nbsp; 1 of 2</div>
  </main>
</body>
</html>
```